Startup Drone Platform Company business card

We are needing a business card design for our employees. We are a startup drone platform. We are looking for a business card that has our logo on one side, with the employee/company details on the opposite side. We are looking for something that is very eye catching, modern, and bold.

Target Market(s)

This will target both drone pilots and drone businesses, along with all the industries that could utilize drone services (aerial video, aerial photos, inspections, 3d mapping, etc).

Industry/Entity Type

Business

```html
<!DOCTYPE html>
<html lang="en">
<head>
<meta charset="utf-8">
<title>Skylane Works – Business Card</title>
<link rel="stylesheet" href="https://fonts.googleapis.com/css2?family=Montserrat:wght@500&family=Saira+Condensed:wght@200;300&display=swap">
<style>
  :root {
    --bg: #e4e4e4;
    --card-front: #2f2f31;
    --card-back: #1d1d1e;
    --card-panel: #343436;
    --ink-light: #f2f2f2;
    --accent-teal: #3fb6c4;
    --accent-red: #a3121f;
    --ink-muted: #0c0c0c;
  }
  * { margin: 0; padding: 0; box-sizing: border-box; }
  html, body { width: 1200px; height: 900px; overflow: hidden; }
  body {
    background: radial-gradient(ellipse at 40% 40%, #f1f1f1 0%, var(--bg) 60%, #cfcfcf 100%);
    position: relative;
    font-family: "Montserrat", sans-serif;
  }
  .card {
    position: absolute;
    left: 290px;
    width: 620px;
    height: 354px;
    overflow: hidden;
    box-shadow: 0 10px 24px rgba(0,0,0,.28);
  }
  .card--front { top: 62px; background: var(--card-front); }
  .card--back { top: 484px; background: var(--card-back); }

  .card__glow { position: absolute; inset: 0; }

  .wordmark {
    position: absolute;
    display: flex;
    align-items: center;
    color: var(--ink-light);
    font-weight: 500;
    text-transform: uppercase;
    white-space: nowrap;
  }
  .wordmark__dot {
    display: inline-block;
    border-radius: 50%;
    background: var(--accent-teal);
  }
  .card--front .wordmark {
    top: 140px; left: 0; right: 0; justify-content: center;
    font-size: 20px; letter-spacing: 0.55em; gap: 14px;
  }
  .card--front .wordmark__dot { width: 16px; height: 16px; margin-right: 8px; }

  .card__panel {
    position: absolute; left: 0; top: 0; bottom: 0; width: 180px;
    background: linear-gradient(160deg, #3a3a3c 0%, var(--card-panel) 60%, #2c2c2e 100%);
  }
  .card__panel .wordmark {
    top: 120px; left: 0; right: 0;
    flex-direction: column; gap: 12px;
    font-size: 15px; letter-spacing: 0.45em;
  }
  .card__panel .wordmark__dot { width: 40px; height: 40px; margin-bottom: 6px; }

  .contact {
    position: absolute; right: 52px; top: 40px;
    text-align: right;
    font-family: "Saira Condensed", sans-serif;
    color: var(--ink-muted);
    line-height: 1.05;
  }
  .contact__address { font-size: 20px; font-weight: 200; letter-spacing: 0.08em; text-transform: uppercase; }
  .contact__phone { font-size: 26px; font-weight: 300; letter-spacing: 0.04em; margin-top: 4px; }
  .divider {
    position: absolute; right: 52px; top: 170px;
    width: 320px; height: 1px; background: var(--accent-teal);
  }
  .person-name {
    position: absolute; right: 40px; bottom: 34px;
    font-family: "Saira Condensed", sans-serif;
    font-weight: 200; font-size: 62px; letter-spacing: 0.03em;
    color: var(--accent-red); text-transform: uppercase;
    white-space: nowrap;
  }
</style>
</head>
<body>
  <section class="card card--front" aria-label="Card front">
    <svg class="card__glow" width="620" height="354" viewBox="0 0 620 354" aria-hidden="true">
      <defs>
        <linearGradient id="edge-glow" x1="0" y1="0" x2="0.25" y2="1">
          <stop offset="0" stop-color="#3fb6c4" stop-opacity="0.9"/>
          <stop offset="1" stop-color="#3fb6c4" stop-opacity="0"/>
        </linearGradient>
      </defs>
      <polygon points="620,200 620,354 330,354" fill="#2a2a2c"/>
      <polygon points="620,200 330,354 350,354 620,214" fill="url(#edge-glow)" opacity="0.55"/>
      <line x1="620" y1="200" x2="330" y2="354" stroke="#3fb6c4" stroke-width="1.5"/>
    </svg>
    <div class="wordmark">
      <span>Skylane</span>
      <span class="wordmark__dot"></span>
      <span>Works</span>
    </div>
  </section>

  <section class="card card--back" aria-label="Card back">
    <div class="card__panel">
      <div class="wordmark">
        <span class="wordmark__dot"></span>
        <span>Skylane</span>
        <span>Works</span>
      </div>
    </div>
    <div class="contact">
      <p class="contact__address">418 N. Harbor Ave</p>
      <p class="contact__address">Denver CO 80202</p>
      <p class="contact__phone">1 - 555 - 555 - 0148</p>
    </div>
    <div class="divider"></div>
    <h1 class="person-name">Daniel Ashgrove</h1>
  </section>
</body>
</html>
```